Weight loss surgery restaurant card

We need to create a card for patients who have undergone weight loss surgery to take to restaurants so they can request smaller meals. These patients have had surgery on their stomach so that they can only consume half to one cup of food at a time. So normal sized restaurant meals are way too big (and cost a lot). This card they can present to the restaurant to communicate the fact that they have had weight loss surgery and therefore request a smaller meal portion at reduced cost

Target Market(s)

Restaurants serving weight loss surgery patients

Industry/Entity Type

Health Care

Contact Information for Business Card

This will be a plastic card similar to business card size.

Requirements
Must have
• The front of the card should include the following text:
• The individual bearing this card has undergone weight loss surgery.
• This surgery restricts portion sizes to between half and one cup of food at a time.
• Please give consideration to allowing smaller portions of your regular meals to be ordered to reduce wastage and excess costs.
• Example: a half size portion priced at two thirds of usual cost.
• The back of the card will have spaces for the person to write certain information. These are the categories that can be filled in by hand:
• Name:
• Procedure performed:
• Date of procedure (month/year):
• Treating Clinic Name:
• Treating Clinic Signature:
• Somewhere down the bottom should be something along the lines of:
• supplied from bernardwhitlow.com.au
Nice to have
• A nice design with imagery/colours etc ... not just the text on a white background! Bright attractive colours preferred.
• I have uploaded my logo ... a roughly triangular image followed by my name etc. The triangular logo image could be used somewhere on the card and this logo can be interchangeable for other clinics who purchase the card.
• **Please note that I don't want my name to be included as part of the logo on the card ... just use the triangular image on the side of the logo without the following name**
• Also, the colouring of the card does not have to reflect my logo colours as I am anticipating interchanging this logo with other logos if other clinics choose to adopt the card. I am interested to see other, more generic, colour choices as well as my logo colours

```html
<!DOCTYPE html>
<html lang="en">
<head>
<meta charset="utf-8">
<title>Smaller Portion Meal Card – Back</title>
<link rel="stylesheet" href="https://fonts.googleapis.com/css2?family=Roboto:wght@400&family=Oswald:wght@500&family=Michroma&display=swap">
<style>
  :root {
    --card-width: 1200px;
    --card-height: 702px;
    --accent-magenta: #a8409a;
    --label-maroon: #7c1d3c;
    --rule-ink: #2b2b2b;
    --panel-white: rgba(255, 255, 255, 0.86);
    --food-warm: #d9b48a;
    --food-green: #7f9a5a;
    --food-red: #a0462e;
    --food-cream: #efe7dc;
    --footer-text: #ffffff;
  }

  * { box-sizing: border-box; margin: 0; padding: 0; }

  html, body {
    width: var(--card-width);
    height: var(--card-height);
    overflow: hidden;
    background: #ffffff;
  }

  .meal-card {
    position: relative;
    width: var(--card-width);
    height: var(--card-height);
    overflow: hidden;
    font-family: "Roboto", Arial, sans-serif;
  }

  .food-backdrop {
    position: absolute;
    inset: 0;
    background:
      radial-gradient(ellipse at 20% 95%, var(--food-green) 0%, transparent 30%),
      radial-gradient(ellipse at 50% 100%, var(--food-red) 0%, transparent 28%),
      radial-gradient(ellipse at 85% 0%, var(--food-red) 0%, transparent 25%),
      radial-gradient(ellipse at 50% 0%, var(--food-green) 0%, transparent 30%),
      linear-gradient(135deg, var(--food-cream) 0%, var(--food-warm) 50%, var(--food-cream) 100%);
  }

  .entry-panel {
    position: absolute;
    left: 0;
    top: 50px;
    width: 100%;
    height: 573px;
    background: var(--panel-white);
    border-top: 2px solid var(--accent-magenta);
    border-bottom: 2px solid var(--accent-magenta);
  }

  .logo-placeholder {
    position: absolute;
    left: 967px;
    top: 91px;
    width: 148px;
    height: 84px;
    border: 2px solid var(--accent-magenta);
    color: var(--accent-magenta);
    font-family: "Oswald", "Arial Narrow", sans-serif;
    font-weight: 500;
    font-size: 31px;
    line-height: 35px;
    letter-spacing: 0;
    white-space: nowrap;
    display: flex;
    flex-direction: column;
    align-items: center;
    justify-content: center;
  }

  .logo-placeholder span { display: block; }

  .entry-fields {
    position: absolute;
    left: 86px;
    top: 204px;
    width: 1029px;
    list-style: none;
  }

  .entry-field {
    display: flex;
    align-items: flex-end;
    height: 83px;
  }

  .entry-field:first-child { height: 40px; }

  .field-label {
    color: var(--label-maroon);
    font-size: 24.5px;
    white-space: nowrap;
    margin-right: 14px;
    line-height: 1;
  }

  .field-rule {
    flex: 1;
    border-bottom: 1.5px solid var(--rule-ink);
    margin-bottom: 1px;
  }

  .supplier-line {
    position: absolute;
    left: 0;
    top: 644px;
    width: 100%;
    text-align: center;
    color: var(--footer-text);
    font-family: "Michroma", "Arial Black", sans-serif;
    font-size: 23px;
    letter-spacing: 0.5px;
    -webkit-text-stroke: 0.8px var(--footer-text);
    text-shadow: 0 0 4px rgba(0,0,0,0.9), 1px 1px 2px rgba(0,0,0,0.9);
  }
</style>
</head>
<body>
  <main class="meal-card">
    <div class="food-backdrop" role="img" aria-label="Overhead photograph of a restaurant table spread with shared dishes"></div>

    <section class="entry-panel" aria-label="Patient details"></section>

    <div class="logo-placeholder"><span>PUT YOUR</span><span>LOGO HERE</span></div>

    <ul class="entry-fields">
      <li class="entry-field"><span class="field-label">Name :</span><span class="field-rule"></span></li>
      <li class="entry-field"><span class="field-label">Procedure performed :</span><span class="field-rule"></span></li>
      <li class="entry-field"><span class="field-label">Date of procedure (month/year) :</span><span class="field-rule"></span></li>
      <li class="entry-field"><span class="field-label">Treating Clinic Name:</span><span class="field-rule"></span></li>
      <li class="entry-field"><span class="field-label">Treating Clinic Signature:</span><span class="field-rule"></span></li>
    </ul>

    <p class="supplier-line">MEAL CARDS AVAILABLE AT BERNARDWHITLOW.COM.AU</p>
  </main>
</body>
</html>
```